Website Design for Door Distributor

Granite Hinge Works LLC distributes doors in the Southwestern region of the United States. We need a website design for our company launch.

We are looking for a website design that screams modern, and is easy to navigate. We want our customers to browse through our collections of doors with ease, while at the same time enjoy the feel of the website (more on how the website should feel below). Our logo is attached to help with the design process.

We expect this relationship to continue beyond the initial assignment, whether it includes additions or updates to the site. In that sense, we will only work with that designer who will specifically incorporate our ideas into the design, not a designer that submits a "one-size-fits-all" design. With that in mind, we are looking for a creative person who is willing to take some risks.

We are committed to minimizing the amount of revisions needed, so we encourage you to message us with any questions you may have throughout the process, especially in the earlier phases.

Thanks in advance for your time.

Target Market(s)

Home builders, commercial builders, developers, and upper-middle class/upper class customers. As you can see, our target market is of a more sophisticated type, so the design should be on the more serious side, and less playful. It should showcase a sense of class.

Industry/Entity Type

Requirements
Must have
• The home page should have a slideshow showcasing 4 to 5 different topics. See www.quillbranch.net for an example. The headings for each picture should be easily customizable (font, color, etc.). The user should also be able to click on the picture and be taken to the page that the pictures are linked to.

At the very top right of every page, there should be 2 header links: Download Brochure | Contact

There should be 5 static categories placed in one row at the top of each page. See www.morvik-tane.com for an example. Each of these categories should drop down when you rest your mouse over it and display a list of links. Again, this should be easily customizable and shown on every page of the site. This will serve as the navigation menu. Let us know if you need to know the exact amount of links for each category - hopefully we can customize it on our end fairly easily.

Categories: Home | Products | Gallery | Support | About Us

Home Page: Along with the above, the home page should include a welcome section that introduces the user to the site. There should also be sections for "Featured Product" and "Testimonial".

Featured product: this will include an image and short text.

Testimonial: this will include a quote, which should be easy for us to update weekly, and a link to "More Testimonials".
Should not have
• No clutter - instead, the design layout should be open and easy to navigate.

No cartoonish graphics - instead, the graphics should be sophisticated and modern.

No flash, no java.

```html
<!DOCTYPE html>
<html lang="en">
<head>
<meta charset="utf-8">
<title>Granite Hinge Works</title>
<link rel="stylesheet" href="https://fonts.googleapis.com/css2?family=Open+Sans:ital,wght@0,400;0,600;1,400&display=swap">
<style>
:root{
  --brown:#6b3a12;
  --brown-dark:#5a2f0c;
  --tan:#a4621c;
  --nav-top:#b06a26;
  --nav-bottom:#7e4412;
  --nav-active:#6a3810;
  --text:#555;
  --muted:#777;
  --line:#dcdcdc;
  --card-line:#e2e2e2;
  --tweet-blue:#2ba7dc;
  --footer:#2c2c2c;
  --footer-text:#bdbdbd;
}
*{margin:0;padding:0;box-sizing:border-box}
html,body{width:798px;height:1200px;overflow:hidden;background:#fff}
body{position:relative;font-family:"Open Sans",Arial,sans-serif;color:var(--text)}
.abs{position:absolute}

/* header */
.brand{left:66px;top:40px;width:140px;color:var(--brown);font-size:19px;font-weight:600;line-height:23px;text-align:center;letter-spacing:1px}
.brand-mark{left:124px;top:14px;width:22px;height:22px;background:var(--tan)}
.util-links{right:68px;top:32px;font-size:10px;color:#444}
.util-links span{color:#aaa;margin:0 5px}
.call{right:96px;top:76px;text-align:right}
.call-label{font-size:13px;color:var(--tan);line-height:15px}
.call-number{font-size:16px;color:var(--brown-dark);font-weight:600;line-height:20px}
.phone-icon{left:708px;top:84px}

/* navigation */
.nav{left:0;top:146px;width:798px;height:34px;background:linear-gradient(var(--nav-top),var(--nav-bottom))}
.nav ul{list-style:none;display:flex;margin-left:66px;height:34px;border-left:1px solid rgba(0,0,0,.2)}
.nav li{color:#fff;font-size:11px;text-transform:uppercase;line-height:34px;padding:0 16px;border-right:1px solid rgba(0,0,0,.2)}
.nav li.active{background:var(--nav-active)}

/* slideshow */
.slide{left:66px;top:191px;width:665px;height:313px;background:linear-gradient(90deg,#7b8a55 0%,#d8b27a 20%,#6b3a1e 45%,#6b3a1e 60%,#d6b07a 82%,#6c7f48 100%)}
.slide-caption{left:0;bottom:0;width:100%;height:41px;background:rgba(20,12,6,.78);color:#fff;font-size:15px;line-height:41px;padding-left:20px}
.slide-arrows{right:14px;top:14px;display:flex;gap:1px}
.slide-arrows div{width:13px;height:13px;background:#fff;display:flex;align-items:center;justify-content:center}

/* welcome */
.welcome-title{left:69px;top:522px;font-size:16px;color:var(--brown)}
.welcome-text{left:69px;top:552px;width:488px;font-size:9.3px;line-height:16.6px;color:var(--text)}
.welcome-photo{left:572px;top:528px;width:158px;height:101px;background:linear-gradient(120deg,#7a4a24,#b27a48 55%,#6e4020)}
.divider{left:66px;top:658px;width:665px;height:1px;background:var(--line)}

/* featured */
.section-title{font-size:16px;color:var(--brown)}
.featured-title{left:67px;top:679px}
.carousel-arrows{left:541px;top:684px;font-size:13px;color:#666;letter-spacing:2px}
.card{width:152px;height:173px;border:1px solid var(--card-line);background:linear-gradient(#fff 70%,#f6f6f6);text-align:center}
.card-door{width:54px;height:98px;margin:12px auto 0}
.card-name{margin-top:16px;font-size:9px;color:var(--tan)}
.card-text{margin-top:3px;font-size:8px;line-height:11px;color:var(--muted);padding:0 12px}
.pager{left:435px;top:1086px;display:flex;gap:5px}
.pager div{width:16px;height:16px;border-radius:50%;background:#ddd;color:#666;font-size:8px;line-height:16px;text-align:center}
.pager .current{background:var(--tan);color:#fff}

/* testimonials */
.testi-title{left:573px;top:679px;display:flex;align-items:center;gap:6px}
.testi-box{left:572px;top:709px;width:159px;height:178px;border:1px solid var(--card-line)}
.quote{padding:12px 14px 0;font-size:9.3px;font-style:italic;line-height:15.3px;color:#666;text-align:center}
.quote b{font-style:normal;font-weight:600;font-size:13px;color:#666}
.quote-author{margin-top:7px;text-align:center;font-size:9px;color:#3a2a1a}
.more{position:absolute;left:0;bottom:0;width:100%;height:22px;background:#e9e9e9;font-size:8.5px;line-height:22px;text-align:center;color:#555}

/* updates */
.tweets-title{left:573px;top:901px;display:flex;align-items:center;gap:5px;color:var(--tweet-blue)}
.tweets-box{left:572px;top:925px;width:159px;height:180px;border:1px solid var(--card-line);background:#f7f7f7}
.tweet{display:flex;gap:8px;padding:14px 10px 0 13px;height:69px;border-bottom:1px solid #fff}
.avatar{flex:none;width:24px;height:24px;background:#8a7564}
.tweet p{font-size:8.2px;line-height:11px;color:#333}
.tweet a{color:var(--tweet-blue);text-decoration:none}
.tweet-input{margin:2px 0 0;height:35px;background:#fff;border-top:1px solid var(--card-line);font-size:7.5px;color:#999;padding:7px 7px}

/* footer */
.footer{left:0;top:1132px;width:798px;height:68px;background:var(--footer)}
.footer-links{left:67px;top:1146px;font-size:8.5px;color:var(--footer-text)}
.footer-links span{margin:0 4px}
.copyright{left:67px;top:1171px;font-size:8.5px;color:var(--footer-text)}
.social{left:668px;top:1156px;display:flex;gap:5px}
.social div{width:18px;height:18px;border-radius:50%;background:#666}
</style>
</head>
<body>

<header>
  <div class="abs brand-mark"></div>
  <div class="abs brand">GRANITE HINGE WORKS</div>
  <div class="abs util-links">Download Brochure<span>/</span>Contact</div>
  <div class="abs call">
    <div class="call-label">Call us Today!</div>
    <div class="call-number">555 014 7720</div>
  </div>
  <svg class="abs phone-icon" width="22" height="16" viewBox="0 0 22 16">
    <path d="M1 6 Q11 -2 21 6 L18 8 L15 5 L7 5 L4 8 Z" fill="var(--brown-dark)"/>
    <path d="M6 7 L16 7 L19 15 L3 15 Z" fill="var(--brown-dark)"/>
    <circle cx="11" cy="11" r="2.5" fill="#fff"/>
  </svg>
</header>

<nav class="abs nav">
  <ul>
    <li>Home</li>
    <li class="active">Products</li>
    <li>Gallery</li>
    <li>Support</li>
    <li>About Us</li>
  </ul>
</nav>

<section class="abs slide" role="img" aria-label="Wooden double entry door with wrought iron glass panels between columns and palms">
  <div class="abs slide-caption">Nulla rutrum nulla id sollicitudin ultricies vestibulum convallis.</div>
  <div class="abs slide-arrows" style="top:auto;bottom:14px">
    <div><svg width="6" height="8"><path d="M5 0 L1 4 L5 8" stroke="#333" fill="none"/></svg></div>
    <div><svg width="6" height="8"><path d="M1 0 L5 4 L1 8" stroke="#333" fill="none"/></svg></div>
  </div>
</section>

<section>
  <h2 class="abs welcome-title" style="font-weight:400">Welcome to Granite Hinge Works</h2>
  <p class="abs welcome-text">Nulla rutrum nulla id sollicitudin ultricies. Duis ut dolor metus. Nunc egestas est ac commodo ultricies. Morbi sollicitudin lobortis auctor. In hac habitasse platea dictumst. Integer vitae augue blandit, dapibus arcu in, vestibulum lacus. Nullam eu quam massa. Nullam facilisis nunc nec semper semper. Aliquam et suscipit erat, vitae iaculis libero. Curabitur sed dapibus nisl. Donec vel mauris ac purus dignissim dignissim non sit amet ligula. Donec ut nisl ut ligula iaculis fermentum at id enim. Mauris euismod lorem in felis lacinia.</p>
  <div class="abs welcome-photo" role="img" aria-label="Hand lifting a brass knocker on a wooden door"></div>
</section>
<div class="abs divider"></div>

<section>
  <h2 class="abs section-title featured-title" style="font-weight:400">Featured Product</h2>
  <div class="abs carousel-arrows">&lsaquo;&rsaquo;</div>

  <div class="abs card" style="left:69px;top:709px"><div class="card-door" role="img" aria-label="Open oak panel door" style="background:linear-gradient(90deg,#e9c9a0,#b8692a 40%,#a85a20)"></div><div class="card-name">Donec vel mauris</div><div class="card-text">Nam vitae tellus tristique, sceleri sque quam eget, egestas dolor.</div></div>
  <div class="abs card" style="left:237px;top:709px"><div class="card-door" role="img" aria-label="Red mahogany panel door" style="width:46px;background:linear-gradient(#9b2a14,#7c1e0e)"></div><div class="card-name">Donec vel mauris</div><div class="card-text">Nam vitae tellus tristique, sceleri sque quam eget, egestas dolor.</div></div>
  <div class="abs card" style="left:405px;top:709px"><div class="card-door" role="img" aria-label="White six panel door" style="width:46px;background:linear-gradient(90deg,#e6e6e6,#f8f8f8,#dcdcdc)"></div><div class="card-name">Donec vel mauris</div><div class="card-text">Nam vitae tellus tristique, sceleri sque quam eget, egestas dolor.</div></div>

  <div class="abs card" style="left:69px;top:897px"><div class="card-door" role="img" aria-label="Honey oak arched panel door" style="width:48px;background:linear-gradient(#c47a2e,#a55e1e)"></div><div class="card-name">Donec vel mauris</div><div class="card-text">Nam vitae tellus tristique, sceleri sque quam eget, egestas dolor.</div></div>
  <div class="abs card" style="left:237px;top:897px"><div class="card-door" role="img" aria-label="Gothic arched wooden door" style="width:44px;border-radius:22px 22px 0 0;background:linear-gradient(#8a5a2a,#5c3512)"></div><div class="card-name">Donec vel mauris</div><div class="card-text">Nam vitae tellus tristique, sceleri sque quam eget, egestas dolor.</div></div>
  <div class="abs card" style="left:405px;top:897px"><div class="card-door" role="img" aria-label="Dark walnut steel clad door" style="width:40px;height:92px;background:linear-gradient(#4a3024,#2e1c14)"></div><div class="card-name">Donec vel mauris</div><div class="card-text">Nam vitae tellus tristique, sceleri sque quam eget, egestas dolor.</div></div>

  <div class="abs pager"><div>&laquo;</div><div class="current">1</div><div>2</div><div>3</div><div>4</div><div>&raquo;</div></div>
</section>

<aside>
  <h2 class="abs section-title testi-title" style="font-weight:400">
    <svg width="20" height="17" viewBox="0 0 20 17"><ellipse cx="10" cy="7" rx="10" ry="7" fill="var(--brown)"/><path d="M3 11 L1 17 L8 13 Z" fill="var(--brown)"/></svg>
    Testimonials
  </h2>
  <div class="abs testi-box">
    <p class="quote"><b>&ldquo;</b> Donec at tempus lectus, eget condimentum neque. Sed commodo eleifend scelerisque. Nunc risus quam, accumsan eu mauris eu, lacinia tincidunt metus. Class aptent taciti sociosqu ad litora <b>&rdquo;</b></p>
    <div class="quote-author">Mara Elling, City</div>
    <div class="more">More Testimonials</div>
  </div>

  <h2 class="abs section-title tweets-title" style="font-weight:400">
    <svg width="17" height="17"><circle cx="8.5" cy="8.5" r="8.5" fill="var(--tweet-blue)"/></svg>
    Tweets
  </h2>
  <div class="abs tweets-box">
    <div class="tweet"><div class="avatar" role="img" aria-label="Member photo"></div><p>Fusce eu lorem dui. Integer eu venen <a>atis lectus</a> sed blandit urna<br><a>@hingeworks</a></p></div>
    <div class="tweet"><div class="avatar" role="img" aria-label="Member photo"></div><p>Fusce eu lorem dui. Integer eu venen <a>atis lectus</a> sed blandit urna<br><a>@hingeworks</a></p></div>
    <div class="tweet-input">Tweet now...</div>
  </div>
</aside>

<footer class="abs footer"></footer>
<div class="abs footer-links">Home<span>|</span>Products<span>|</span>Gallery<span>|</span>Support<span>|</span>About Us<span>|</span>Download Brochure<span>|</span>Contact</div>
<div class="abs copyright">Copyright &copy; 2013 &nbsp;Granite Hinge Works. &nbsp;All rights reserved.</div>
<div class="abs social"><div></div><div></div><div></div></div>

</body>
</html>
```